Vostrel Holdings Web Design

Vostrel Holdings Limited Shenzhen

This project is a 10 page launch website.
Our client is seeking a contemporary homepage design for a Holdings company. Once we are happy with the homepage design and select designer we will request a secondary page design.

Please see attached company LOGO for an idea of style, it incorporates the traditional Chinese furniture lattice work. The Quillmoor website is one of our clients favorite so we would like to see a similar homepage design to this website.

Use the websites below for reference purpose. The first two are Chinese and the second two are international. We would like to see elements of both but more focus on international design.

http://www.evergrande.com/http://www.brevandgroup.com/pub/default.aspx http://www.quillmoor.com/zh/maldives_resortone/
http://www.vellune-studio.com
http://media-cache-ec0.fotrelix.com/originals/41/a3/90/41a390c1f5b7d2e8a6c4f0b9e3d71a55.jpg

Company Background
VOSTREL HOLDINGS, located in Qianhai, China, is a new real-estate project operator, structuring urban-rural real-estate investment and development, and industrial fund investment. The company also invests in supply chain management and supporting infrastructures. To create new spaces and livable cities Vostrel Holdings develop win-win strategic partnerships with a number of institutions. Currently cooperating with Harrow East Lindcombe, China urban and rural integrated demonstration.

Target Market(s)

B2B property investment. Target market customers are senior level management/decision makers of large corporations. Focusing geographically on the domestic market first and expanding internationally in 2nd and 3rd years.

Industry/Entity Type

Investment

Requirements
Must have
• Since this is a new company, we would like to the website representing growth and power, E.g. like a growing tree.
Should not have
• Low-level vectors such as curency symbols, American dollar.

```html
<!DOCTYPE html>
<html lang="en">
<head>
<meta charset="utf-8">
<title>Vostrel Holdings</title>
<link href="https://fonts.googleapis.com/css2?family=Ubuntu:wght@300;400;500;700&display=swap" rel="stylesheet">
<style>
:root{
  --page:#ffffff;
  --floor:#b3b3b3;
  --ink:#1e1a1b;
  --ink-deep:#131011;
  --green:#7dbd1e;
  --green-dark:#2f9a2f;
  --text:#333333;
  --muted:#8a8a8a;
  --footer-text:#dcdcdc;
  --rule:#3a3537;
  --fb:#1a9bd7;
  --tw:#7dbd1e;
  --li:#e3131b;
  --sepia-light:#d6cfc9;
  --sepia-mid:#bdb3ac;
  --sepia-dark:#a69c95;
}
*{margin:0;padding:0;box-sizing:border-box}
html,body{width:1200px;height:999px;overflow:hidden}
body{background:var(--page);font-family:'Ubuntu',sans-serif;position:relative}
.floor{position:absolute;left:0;top:975px;width:1200px;height:24px;background:var(--floor)}
.site{position:absolute;left:183px;top:0;width:827px;height:975px}
.abs{position:absolute}

/* header */
.header{left:0;top:0;width:827px;height:102px;background:var(--ink)}
.brand{left:100px;top:0;width:138px;height:154px;background:var(--ink);z-index:5}
.brand-inner{position:absolute;left:5px;top:3px;width:128px;height:146px;background:#fff;
  display:flex;flex-direction:column;align-items:center;justify-content:center;gap:10px}
.brand-mark{width:40px;height:40px;border-radius:50%;background:#b8923a}
.brand-name{font-size:12px;font-weight:400;color:#b8923a;letter-spacing:.3px;text-align:center;line-height:1.2}
.call{left:586px;top:20px;font-size:8.5px;color:var(--muted);font-weight:300}
.social{left:669px;top:17px}
.nav{left:326px;top:52px;height:34px;display:flex;align-items:center;font-size:9px;font-weight:500;color:#fff;letter-spacing:.2px}
.nav .sep{width:1px;height:9px;background:#fff}
.nav a{color:#fff;text-decoration:none;height:34px;display:flex;align-items:center;justify-content:center}
.nav a.active{background:var(--green);color:var(--ink);font-weight:700}

/* hero */
.hero{left:0;top:102px;width:827px;height:310px;
  background:
   radial-gradient(ellipse 90px 120px at 665px 120px,rgba(255,255,255,.85) 0%,rgba(255,255,255,0) 100%),
   radial-gradient(ellipse 230px 300px at 700px 150px,#6cbc34 0%,#9bd06f 50%,rgba(190,228,170,0) 80%),
   linear-gradient(110deg,#dcefee 0%,#e6f3ec 35%,#e2f1dc 55%,#a8d884 78%,#6ab82e 100%)}
.hero-shadow{left:0;top:412px;width:827px;height:6px;background:linear-gradient(#bdbdbd,#fff)}
.hero-title{left:154px;top:206px;font-size:34px;font-weight:700;color:var(--green-dark);letter-spacing:-.3px}
.hero-copy{left:155px;top:245px;font-size:12.6px;line-height:18px;color:var(--text)}
.arrow{width:30px;height:30px;border-radius:50%;background:#fff;display:flex;align-items:center;justify-content:center;box-shadow:0 0 6px rgba(0,0,0,.15)}

/* grid */
.tile{width:201px;height:141px}
.tile-photo{width:201px;height:117px;
  background:
   radial-gradient(ellipse 40px 70px at 96px 60px,rgba(150,138,128,.55) 0%,rgba(150,138,128,0) 100%),
   linear-gradient(var(--sepia-light),var(--sepia-mid) 55%,var(--sepia-dark) 80%,var(--sepia-light))}
.tile-bar{width:201px;height:5px;background:#4a4849}
.tile-reflect{width:201px;height:19px;background:linear-gradient(#d9d9d9,#fff)}
.tile.feature .tile-photo{position:relative;
  background:linear-gradient(#6dbb3c,#9fd07e 45%,#dcebc8 80%,#eef3de)}
.feature-band{position:absolute;left:0;top:63px;width:201px;height:54px;background:rgba(255,255,255,.5);
  display:flex;align-items:center;justify-content:center;text-align:center;font-size:11px;font-weight:700;color:#2a8a2a;line-height:12px}

/* footer */
.footer{left:0;top:781px;width:827px;height:156px;background:var(--ink)}
.legal{left:0;top:937px;width:827px;height:38px;background:var(--ink-deep);text-align:center;font-size:7px;line-height:9px;color:var(--footer-text);padding-top:12px}
.fcol{top:18px}
.fcol h3{font-size:11px;font-weight:700;color:#fff;margin-bottom:11px;letter-spacing:.1px}
.links{list-style:none;width:121px;border-top:1px solid var(--rule)}
.links li{font-size:8px;color:var(--footer-text);height:15.5px;line-height:14px;border-bottom:1px solid var(--rule)}
.contact{font-size:8px;line-height:11.3px;color:var(--footer-text);padding-top:4px}
</style>
</head>
<body>
<div class="floor"></div>
<div class="site">
  <header class="abs header">
    <div class="abs call">call : 0000 000 000</div>
    <svg class="abs social" width="56" height="16" viewBox="0 0 56 16" aria-label="Social links">
      <circle cx="7" cy="8" r="7" fill="var(--fb)"/>
      <circle cx="27" cy="8" r="7" fill="var(--tw)"/>
      <circle cx="46" cy="8" r="7" fill="var(--li)"/>
    </svg>
    <nav class="abs nav">
      <span class="sep"></span><a style="width:67px">HOME</a>
      <span class="sep"></span><a style="width:83px">ABOUT US</a>
      <span class="sep"></span><a style="width:94px">CONTACT US</a>
      <span class="sep"></span><a class="active" style="width:88px">PORTFOLIO</a>
      <span class="sep"></span><a style="width:59px">HELP</a>
      <span class="sep"></span>
    </nav>
  </header>
  <div class="abs brand">
    <div class="brand-inner">
      <div class="brand-mark"></div>
      <div class="brand-name">Vostrel Holdings</div>
    </div>
  </div>

  <section class="abs hero" role="img" aria-label="Growing tree: a young green sapling sprouting from a light bulb base, symbolising growth and power, on a soft green background"></section>
  <h1 class="abs hero-title">welcome to</h1>
  <p class="abs hero-copy">lorem ipsum dolor lorem ipsum dolor<br>lorem ipsum dolor<br>lorem ipsum dolor lorem ipsum dolor lorem ipsum dolor</p>
  <div class="abs arrow" style="left:88px;top:243px"><svg width="10" height="14" viewBox="0 0 10 14"><path d="M8 1 2 7l6 6" fill="none" stroke="#222" stroke-width="2.4"/></svg></div>
  <div class="abs arrow" style="left:709px;top:243px"><svg width="10" height="14" viewBox="0 0 10 14"><path d="M2 1l6 6-6 6" fill="none" stroke="#222" stroke-width="2.4"/></svg></div>
  <svg class="abs" style="left:392px;top:386px" width="44" height="11" viewBox="0 0 44 11">
    <circle cx="5.5" cy="5.5" r="5" fill="var(--ink)"/>
    <circle cx="21" cy="5.5" r="5" fill="var(--green)"/>
    <circle cx="37" cy="5.5" r="5" fill="var(--ink)"/>
  </svg>
  <div class="abs hero-shadow"></div>

  <div class="abs tile" style="left:104px;top:458px"><div class="tile-photo" role="img" aria-label="Sepia photo of a young seedling growing from the soil"></div><div class="tile-bar"></div><div class="tile-reflect"></div></div>
  <div class="abs tile" style="left:313px;top:458px"><div class="tile-photo" role="img" aria-label="Sepia photo of a young seedling growing from the soil"></div><div class="tile-bar"></div><div class="tile-reflect"></div></div>
  <div class="abs tile" style="left:522px;top:458px"><div class="tile-photo" role="img" aria-label="Sepia photo of a young seedling growing from the soil"></div><div class="tile-bar"></div><div class="tile-reflect"></div></div>
  <div class="abs tile" style="left:104px;top:611px"><div class="tile-photo" role="img" aria-label="Sepia photo of a young seedling growing from the soil"></div><div class="tile-bar"></div><div class="tile-reflect"></div></div>
  <div class="abs tile feature" style="left:313px;top:611px"><div class="tile-photo" role="img" aria-label="Green tinted photo of a young seedling growing from the soil"><div class="feature-band">REPRESENTING<br>GROWTH AND POWER</div></div><div class="tile-bar"></div><div class="tile-reflect"></div></div>
  <div class="abs tile" style="left:522px;top:611px"><div class="tile-photo" role="img" aria-label="Sepia photo of a young seedling growing from the soil"></div><div class="tile-bar"></div><div class="tile-reflect"></div></div>

  <footer class="abs footer">
    <div class="abs fcol" style="left:104px">
      <h3>QUICK LINK</h3>
      <ul class="links"><li>Home</li><li>About Us</li><li>Contact Us</li><li>Portfolio</li><li>Help</li><li>Faq</li></ul>
    </div>
    <div class="abs fcol" style="left:365px">
      <h3>TERMS &amp; PRIVACY</h3>
      <ul class="links"><li>Terms of use</li><li>Privacy Policty</li><li>Information</li></ul>
    </div>
    <div class="abs fcol" style="left:626px">
      <h3>CONTACT INFO</h3>
      <p class="contact">Street Address<br>1122 Fernway Outlook<br>United States of America<br><br>ph : 0000 000 0000<br>email : id@vostrelweb.com<br>web : www.vostrelweb.com</p>
    </div>
  </footer>
  <div class="abs legal">Copyright © 2013 VostrelHoldings<br>*Conditions apply please see our terms and privacy page.</div>
</div>
</body>
</html>
```